Website for New Medical Professional Organization Anti-Aging

Thanks to all who participated in my logo design project! We had several very good options to choose from, but we decided to go with the project attached by Marel.

Now, we need to develop the same idea into a web page. Our membership will be professionals involved in anti-aging medicine including doctors, naturopaths, chiropractors, nurses, nurse practioners, etc and also the corporations that have an interest eg. testing facilities, pharmacies, etc.

The sections will be :\
About Us
Membership
Certification
Conferences
Directory
Classifieds
Community

We need at least 2 areas for pictures that change content. One large one smaller.

1. Banner for the top, which includes the Logo, social media contacts, phone number, website address www.vbrelm.ca. We are thinking of using the black backround for the banner, then white backround with black and gold headings for the body.

2. Banner for footer: black again with small logo and contact information

3. The corporate sponsor banner can go across the bottom just above the footer banner. This one can be moving right to left to reveal the corporate sponsor names.

We need a section for "Join Now" where they are lead to a place to enter name, profession, address, email, phone, etc.

We need a nice looking "cart" for purchases on the webpage...

Our competition (and leader in the field is www.k7q.com. We like some of their ideas, but it looks disorganized and too commercial. We want to look professional but friendly and interesting.

I am hoping that you all can "see" the logo on the black backround ... I can't see it on mine because I don't have editing software... I really like the gold logo on black as the designer provided.

Thanks and good luck!

I chose a gold colour from the colour wheel, but what I really want is for the logo colour to be present in the website design and become a prominent part of the design. Thanks for your work so far!

Lorna

Hello designers!

I really like the ones that have more black in them. I would like to see more use of the Logo - make it bigger and a more integral pat of the website design. Since we are Canadian, we probably should have some red somewhere too :) So, now I am thinking Gold, Black, White and Red. I am not liking the silver I have seen so far. Please try to make the gold more regal and glowing. Thanks!

Lorna

Target Market(s)

professionals - doctors, chiropractors, naturopaths, nurses
commercial health providers - pharmacy, testing facilities, etc

Industry/Entity Type

Nurse

Colors
ffcf3e
000000
d5d5d5

Requirements
Must have
• social media
contact info
e commerce

```html
<!DOCTYPE html>
<html lang="en">
<head>
<meta charset="utf-8">
<title>Northern Society of Vitality Medicine</title>
<link href="https://fonts.googleapis.com/css2?family=Cinzel:wght@400;600&family=Sorts+Mill+Goudy:ital@0;1&family=Open+Sans:wght@400;600&display=swap" rel="stylesheet">
<style>
:root{
  --gold:#b8862e;
  --gold-light:#e9c46a;
  --gold-dark:#7a5618;
  --black:#000;
  --panel:#0d0d0d;
  --red:#f20000;
  --grey:#a8a8a8;
  --light:#d5d5d5;
  --text-dim:#c9c9c9;
  --text-body:#555;
  --white:#fff;
}
*{box-sizing:border-box;margin:0;padding:0}
html,body{width:1110px;height:1200px;overflow:hidden}
body{
  position:relative;
  background:linear-gradient(180deg,#2a2a2a 0%,#3a3a3a 35%,#1d1d1d 55%,#141414 100%);
  font-family:"Open Sans",Arial,sans-serif;
}
.backdrop{position:absolute;inset:0;background:radial-gradient(ellipse at 50% 40%,rgba(90,90,90,.35),rgba(0,0,0,0) 70%)}
.site{
  position:absolute;left:149px;top:26px;width:812px;height:1142px;
  border:3px solid var(--gold);border-radius:10px;background:var(--black);
  box-shadow:0 0 18px rgba(0,0,0,.8);overflow:visible;
}
.abs{position:absolute}

/* header */
.brand{left:26px;top:20px;display:flex;align-items:center;gap:14px}
.brand-mark{width:58px;height:58px;border-radius:50%;background:var(--gold)}
.brand-name{font-family:"Cinzel",serif;color:var(--gold);font-size:22px;line-height:24px;font-weight:400}
.member-bar{right:22px;top:14px;height:18px;padding:0 6px;background:var(--gold);color:#1a1206;font-size:10.5px;line-height:18px;display:flex;align-items:center;gap:5px}
.social{right:22px;top:46px;display:flex;gap:7px}
.social span{width:22px;height:22px;border-radius:50%;display:block}
.social .s1{background:#d22}.social .s2{background:#3b5a9a}.social .s3{background:#2aa3e0}
.call{right:22px;top:74px;font-family:"Sorts Mill Goudy",serif;color:var(--gold);font-size:23px;font-weight:700;letter-spacing:.2px}

/* nav */
.nav{left:-13px;top:105px;width:835px;height:30px;
  background:linear-gradient(180deg,#f3d88a 0%,#d4a94a 45%,#a5772a 100%);
  border-top:1px solid #fbe8b0;border-bottom:1px solid #6a4a14;
  display:flex;align-items:stretch;padding-left:35px}
.nav a{color:#4a3410;text-decoration:none;font-family:Arial,sans-serif;font-size:14px;line-height:29px;padding:0 11px;text-shadow:0 1px 0 rgba(255,240,200,.6)}
.nav a.active{background:var(--red);color:var(--white);text-shadow:none;padding:0 14px}

/* hero */
.hero{left:22px;top:148px;width:762px;height:316px;overflow:hidden}
.hero-photo{position:absolute;inset:0;background:linear-gradient(180deg,#a9bdd0 0%,#8b97a1 30%,#6d6f72 60%,#8a6f52 100%)}
.hero-panel{position:absolute;left:0;top:0;width:292px;height:316px;background:linear-gradient(180deg,rgba(235,235,235,.92),rgba(220,210,200,.88));text-align:center;font-family:"Sorts Mill Goudy",serif;color:#111}
.hero-title{margin-top:46px;font-size:23px;line-height:24px}
.hero-event{font-size:42px;line-height:46px;color:var(--gold);font-weight:700}
.hero-quote{position:relative;margin:12px auto 0;width:240px;font-style:italic;font-size:22px;line-height:28px}
.hero-quote .q{position:absolute;font-size:62px;color:#777;font-style:normal;line-height:1}
.hero-quote .q1{left:-6px;top:-10px}.hero-quote .q2{right:-6px;top:52px}
.hero-date{position:absolute;left:0;right:0;top:307px;font-size:13.5px}
.hero-date{top:268px}
.dots{position:absolute;left:418px;top:353px;display:flex;gap:8px}
.dots span{width:10px;height:10px;border-radius:50%;background:var(--white)}
.dots span.on{background:var(--red)}

/* welcome */
.welcome{left:0;top:464px;width:806px;height:157px;background:linear-gradient(180deg,#1b1b1b 0%,#0b0b0b 20%,#0b0b0b 100%)}
.welcome h2{position:absolute;left:33px;top:40px;font-family:"Sorts Mill Goudy",serif;font-weight:400;color:var(--gold);font-size:25px}
.welcome p{position:absolute;left:33px;top:78px;width:590px;color:var(--text-dim);font-size:12.6px;line-height:20px}
.btn{position:absolute;display:block;text-align:center;font-family:"Sorts Mill Goudy",serif;color:var(--white);text-decoration:none}
.btn-join{left:651px;top:40px;width:140px;height:37px;line-height:37px;background:var(--red);font-size:15px}
.btn-learn{left:651px;top:92px;width:140px;height:37px;line-height:37px;background:var(--grey);font-size:15px}

/* feature */
.feature{left:0;top:621px;width:806px;height:420px;background:var(--white)}
.feature-photo{position:absolute;left:22px;top:33px;width:310px;height:218px;background:linear-gradient(180deg,#cfd3d6 0%,#7d7f84 45%,#3b3d42 100%)}
.feature h1{position:absolute;left:360px;top:30px;font-family:"Sorts Mill Goudy",serif;font-weight:400;color:#8f6420;font-size:27px}
.feature p{position:absolute;left:360px;width:425px;color:var(--text-body);font-size:12.6px;line-height:20px}
.p1{top:76px}.p2{top:143px}
.shop{position:absolute;left:360px;top:204px;display:flex;height:36px;text-decoration:none}
.shop .label{width:94px;background:var(--red);color:var(--white);font-family:"Sorts Mill Goudy",serif;font-size:13px;line-height:36px;text-align:center}
.shop .icon{width:43px;background:#111;display:flex;align-items:center;justify-content:center}

.sponsors-title{position:absolute;left:0;right:0;top:325px;text-align:center;font-family:"Sorts Mill Goudy",serif;color:var(--gold);font-size:20px}
.sponsors{position:absolute;left:0;top:365px;width:806px;height:40px}
.arrow{position:absolute;top:6px}
.arrow-l{left:22px}.arrow-r{left:773px}
.sponsor{position:absolute;top:8px;display:flex;align-items:center;gap:8px;font-family:"Open Sans",sans-serif;font-size:20px;color:#333}
.sponsor i{display:block;width:20px;height:20px;background:#333;border-radius:50%}
.sponsor.s-a{left:58px}.sponsor.s-b{left:258px}.sponsor.s-c{left:430px}.sponsor.s-d{left:610px}

/* footer */
.footer{left:0;top:1041px;width:806px;height:98px;background:var(--black)}
.f-head{position:absolute;font-family:"Sorts Mill Goudy",serif;color:var(--gold);font-size:13.5px;font-weight:700;letter-spacing:.3px}
.f-list{position:absolute;color:var(--text-dim);font-size:11px;line-height:16px;list-style:none}
.f-brand{position:absolute;left:528px;top:18px;display:flex;align-items:center;gap:9px}
.f-brand i{display:block;width:36px;height:36px;border-radius:50%;background:var(--gold)}
.f-brand span{font-family:"Cinzel",serif;color:var(--gold);font-size:14px;line-height:15px}
.f-copy{position:absolute;right:22px;top:73px;color:var(--text-dim);font-size:10.5px}
</style>
</head>
<body>
<div class="backdrop" role="img" aria-label="Dark city skyline across the water"></div>

<div class="site">
  <header>
    <div class="abs brand">
      <span class="brand-mark"></span>
      <div class="brand-name">Northern Society<br>of Vitality Medicine</div>
    </div>
    <div class="abs member-bar">Members Log-in | Cart
      <svg width="14" height="12" viewBox="0 0 14 12"><path d="M0 1h2.5l1.8 6.5h7.2L13 3H4" fill="none" stroke="#1a1206" stroke-width="1.4"/><circle cx="5" cy="10.3" r="1.2" fill="#1a1206"/><circle cx="10.5" cy="10.3" r="1.2" fill="#1a1206"/></svg>
    </div>
    <div class="abs social" aria-label="Social media links"><span class="s1"></span><span class="s2"></span><span class="s3"></span></div>
    <div class="abs call">call now: 012-345-7890</div>
  </header>

  <nav class="abs nav">
    <a href="#">Home</a><a href="#">About Us</a><a href="#" class="active">Membership</a><a href="#">Certification</a><a href="#">Conferences</a><a href="#">Directory</a><a href="#">Classifieds</a><a href="#">Community</a><a href="#">Contact</a>
  </nav>

  <section class="abs hero">
    <div class="hero-photo" role="img" aria-label="Aerial view of the Montreal skyline in autumn"></div>
    <div class="hero-panel">
      <div class="hero-title">Northern Society of<br>Vitality Medicine</div>
      <div class="hero-event">Symposium</div>
      <div class="hero-quote"><span class="q q1">&ldquo;</span>Applying Functional Medicine to Restore Patient Health<span class="q q2">&rdquo;</span></div>
      <div class="hero-date">October 20, 2014 &nbsp;|&nbsp; Montreal, Canada</div>
    </div>
    <div class="dots"><span></span><span class="on"></span><span></span></div>
  </section>

  <section class="abs welcome">
    <h2>Welcome to Northern Society of Vitality Medicine</h2>
    <p>Some sub text ut perspiciatis unde omnis iste natus error sit voluptatem each quesa lorem it. Nemo its enim ipsam voluptatem quia volup tas sit aspernatur aut odit aut fugit. Essed quia consequuntur magni doluptatem sequi nesciunt Neque porro quisquam est, qui dolorem ipsum quia.</p>
    <a href="#" class="btn btn-join">JOIN NOW</a>
    <a href="#" class="btn btn-learn">LEARN MORE</a>
  </section>

  <section class="abs feature">
    <div class="feature-photo" role="img" aria-label="Professionals seated at a conference"></div>
    <h1>H1 Header with Cart Icon Button</h1>
    <p class="p1">Sed ut perspiciatis unde omnis iste natus error sit voluptatem each que sa quae ab illo inventore veritatis et quasi architecto bea tae vitae dicta sunt explicabo. Nemo enim ipsam voluptatem quia volup tas sit.</p>
    <p class="p2">Aspernatur aut odit aut fugit sed quia consequuntur magni doluptatem sequi nesciunt Neque porro quisquam est, qui dolorem ipsum quia.</p>
    <a href="#" class="shop"><span class="label">SHOP NOW</span><span class="icon">
      <svg width="22" height="18" viewBox="0 0 22 18"><path d="M1 2h3.5l2.6 9h10.5L20 4.5H6" fill="none" stroke="#fff" stroke-width="2"/><circle cx="8.5" cy="15" r="1.7" fill="#fff"/><circle cx="16" cy="15" r="1.7" fill="#fff"/></svg></span></a>

    <div class="sponsors-title">NSVM Sponsors</div>
    <div class="sponsors">
      <svg class="arrow arrow-l" width="12" height="24" viewBox="0 0 12 24"><path d="M10 2L2 12l8 10" fill="none" stroke="#e02020" stroke-width="2"/></svg>
      <div class="sponsor s-a"><i></i>Qorvel Lab</div>
      <div class="sponsor s-b"><i></i>Tenwick</div>
      <div class="sponsor s-c">Halvern Diagnostics</div>
      <div class="sponsor s-d"><i></i>Corelan MD</div>
      <svg class="arrow arrow-r" width="12" height="24" viewBox="0 0 12 24"><path d="M2 2l8 10-8 10" fill="none" stroke="#e02020" stroke-width="2"/></svg>
    </div>
  </section>

  <footer class="abs footer">
    <div class="f-head" style="left:22px;top:18px">PAGES</div>
    <ul class="f-list" style="left:22px;top:37px"><li>Home</li><li>About Us</li><li>Classifieds</li></ul>
    <ul class="f-list" style="left:93px;top:37px"><li>Membership</li><li>Certification</li><li>Community</li></ul>
    <ul class="f-list" style="left:180px;top:37px"><li>Conferences</li><li>Directory</li><li>FAQ</li></ul>
    <div class="f-head" style="left:290px;top:18px">CONTACT DETAILS</div>
    <ul class="f-list" style="left:290px;top:37px"><li>p: +123 456 7890 &nbsp;f: +123 456 7891</li><li>PO Box 123, Main City Address Here</li><li>My City and Country, 2331</li></ul>
    <div class="f-brand"><i></i><span>Northern Society<br>of Vitality Medicine</span></div>
    <div class="f-copy">Copyright © NSVM 2014 All Rights Reserved</div>
  </footer>
</div>
</body>
</html>
```